Birchline Septic Solutions

Would like to see some single sided ones but would also like to see some double sided with one sided only being the logo. Owners name is Tom Halvick. Phone number is 555-214-0387
Services are pumping, inspections, installs, and repairs

Contact Information for Business Card

555-241-0387 Tom Halvick Alder Falls, OH

```html
<!DOCTYPE html>
<html lang="en">
<head>
<meta charset="utf-8">
<title>Birchline Septic Solutions – Business Cards</title>
<link href="https://fonts.googleapis.com/css2?family=Open+Sans:wght@400;600;700;800&display=swap" rel="stylesheet">
<style>
  :root {
    --backdrop: #242424;
    --teal: #29bfba;
    --teal-deep: #1f8f8b;
    --card-dark: #222226;
    --white: #ffffff;
    --soft-white: #e9eef0;
  }
  * { margin: 0; padding: 0; box-sizing: border-box; }
  html, body { width: 1200px; height: 779px; overflow: hidden; }
  body {
    background: var(--backdrop);
    font-family: "Open Sans", Arial, sans-serif;
    position: relative;
  }
  .card {
    position: absolute;
    top: 232px;
    width: 540px;
    height: 315px;
    border-radius: 24px;
    overflow: hidden;
    box-shadow: 0 14px 30px rgba(0,0,0,.55);
  }
  .card--front { left: 30px; background: var(--teal); }
  .card--back  { left: 630px; background: var(--card-dark); }

  /* Front: name lockup centred */
  .front-lockup {
    position: absolute; inset: 0;
    display: flex; align-items: center; justify-content: center; gap: 14px;
  }
  .brand-dot {
    width: 22px; height: 22px; border-radius: 50%;
    background: var(--teal-deep);
  }
  .brand-name {
    font-weight: 800;
    color: var(--teal-deep);
    font-size: 30px;
    letter-spacing: 1px;
    line-height: 1.1;
    text-transform: uppercase;
  }

  /* Back */
  .back-brand {
    position: absolute; left: 36px; top: 104px; width: 200px;
    font-weight: 800; color: var(--white);
    font-size: 22px; line-height: 1.15; text-transform: uppercase;
    letter-spacing: .5px;
  }
  .divider {
    position: absolute; left: 262px; top: 62px;
    width: 1px; height: 150px; background: var(--soft-white);
    transform: rotate(-14deg); transform-origin: top center;
  }
  .contact { position: absolute; left: 300px; top: 72px; }
  .contact__name { font-size: 26px; font-weight: 700; line-height: 1.1; }
  .contact__first { color: var(--teal); }
  .contact__last { color: var(--white); }
  .contact__town { color: var(--white); font-size: 15px; margin-top: 6px; }
  .contact__phone {
    color: var(--white); font-size: 15px; margin-top: 4px;
    display: flex; align-items: center; gap: 7px;
  }
  .contact__phone svg { width: 14px; height: 14px; }

  .services {
    position: absolute; left: 0; right: 0; bottom: 38px;
    text-align: center; color: var(--white); font-size: 15px;
  }
  .services__tag {
    display: inline-block; background: var(--teal); color: var(--white);
    font-weight: 600; font-size: 13px; padding: 2px 16px; border-radius: 50%;
    margin-bottom: 10px; text-transform: uppercase;
  }
  .services__list { display: flex; justify-content: center; gap: 12px; }
  .services__item { display: flex; align-items: center; gap: 6px; }
  .services__item::before {
    content: ""; width: 9px; height: 9px; border-radius: 50%; background: var(--teal);
  }
</style>
</head>
<body>
  <section class="card card--front" aria-label="Card front">
    <div class="front-lockup">
      <span class="brand-dot"></span>
      <span class="brand-name">Birchline<br>Septic Solutions</span>
    </div>
  </section>

  <section class="card card--back" aria-label="Card back">
    <div class="back-brand">Birchline Septic Solutions</div>
    <div class="divider"></div>
    <div class="contact">
      <div class="contact__name"><span class="contact__first">Tom</span> <span class="contact__last">Halvick</span></div>
      <div class="contact__town">Alder Falls, OH</div>
      <div class="contact__phone">
        <svg viewBox="0 0 24 24" aria-hidden="true"><path fill="#29bfba" d="M6.6 10.8a15.1 15.1 0 0 0 6.6 6.6l2.2-2.2a1 1 0 0 1 1-.25 11.4 11.4 0 0 0 3.6.57 1 1 0 0 1 1 1V20a1 1 0 0 1-1 1A17 17 0 0 1 3 4a1 1 0 0 1 1-1h3.5a1 1 0 0 1 1 1c0 1.25.2 2.45.57 3.57a1 1 0 0 1-.25 1z"/></svg>
        555-241-0387
      </div>
    </div>
    <div class="services">
      <div class="services__tag">Services</div>
      <div class="services__list">
        <span class="services__item">Pumping</span>
        <span class="services__item">Inspections</span>
        <span class="services__item">Installs</span>
        <span class="services__item">And Repairs</span>
      </div>
    </div>
  </section>
</body>
</html>
```